Fernhollow Advisory Powerpoint Template

We require a powerpoint template, including an appropriate colour palette, for our marketing consultancy called "Fernhollow Advisory". We specialise in B2B Marketing & Innovation strategy for the life sciences and digital healthcare industries.
Our logo has already been designed and we have adopted two font styles for our communications so far: Bebas Neue and Bitter.
Our brand is heavily based around a contemporary industrial style and incorporates elements from east Londons design scene. In fact, our logo and brand was inspired by the street signs around old street in east London. Currently we use a template that uses various grey, black and off-white tones to reflect a industrial style and would like to keep clean creative innovative style. However, we are open to seeing additional colour proposals, as long as they retain the modern industrial feel.

Industry/Entity Type

Business Consultant

Colors

Designer to choose colors to be used in the design.

Requirements
Must have
• Our logo has already been designed and we have adopted two font styles for our communications so far: Bebas Neue and Bitter.
• Our brand is heavily based around a contemporary industrial style and incorporates elements from east Londons design scene. In fact, our logo and brand was inspired by the street signs around old street in east London.
• creative shapes and images to drop in
Nice to have
• owever, we are open to seeing additional colour proposals, as long as they retain the modern industrial feel
Should not have
• too corporate,

```html
<!DOCTYPE html>
<html lang="en">
<head>
<meta charset="utf-8">
<title>Fernhollow Advisory — Presentation Template</title>
<link rel="stylesheet" href="https://fonts.googleapis.com/css2?family=Bebas+Neue&family=Oswald:wght@300;400&display=swap">
<style>
  :root{
    --ink:#141414;
    --coal:#262626;
    --slate:#3a3a3a;
    --smoke:#6b6b6b;
    --ash:#bdbdbd;
    --sand:#d6ccbf;
    --gold:#cda448;
    --paper:#ffffff;
    --muted:#8d8d8d;
  }
  *{box-sizing:border-box;margin:0;padding:0}
  html,body{width:908px;height:1200px;overflow:hidden;background:var(--paper)}
  .deck{
    width:908px;height:1200px;padding:1px 4px;
    display:grid;grid-template-columns:repeat(3,296px);grid-template-rows:repeat(7,166px);gap:6px;
  }
  .slide{position:relative;overflow:hidden;background:var(--paper);box-shadow:0 0 0 .5px #e2e2e2}
  .bg-black{background:var(--ink)}
  .bg-ash{background:var(--ash)}
  .bg-gold{background:var(--gold)}
  .bg-coal{background:var(--coal)}
  .abs{position:absolute}

  /* brand name */
  .logo{position:absolute;display:flex;align-items:center;gap:.3em;font-family:"Bebas Neue",sans-serif;color:var(--ink);line-height:1;letter-spacing:.04em;white-space:nowrap}
  .logo-square{width:.55em;height:.55em;background:currentColor;display:block}
  .logo.light{color:#fff}
  .logo.center{left:50%;top:50%;transform:translate(-50%,-50%)}

  .display{position:absolute;font-family:"Bebas Neue",sans-serif;color:var(--ink);line-height:1;white-space:nowrap}
  .subline{position:absolute;font-family:"Bebas Neue",sans-serif;font-size:4.5px;color:var(--ink);letter-spacing:.02em}
  .rule{position:absolute;height:.6px;background:var(--slate)}

  .title{position:absolute;left:12px;top:12px;font-family:"Bebas Neue",sans-serif;font-size:13px;color:var(--ink);line-height:1}
  .title::after{content:"";display:block;width:14px;height:1.4px;background:var(--gold);margin-top:2px}

  .header{position:absolute;font-family:"Bebas Neue",sans-serif;font-size:5.4px;color:var(--ink);letter-spacing:.02em;line-height:1.2}
  .label{font-family:"Bebas Neue",sans-serif;font-size:4.6px;color:var(--ink);letter-spacing:.03em;line-height:1.1}
  .label.gold{color:var(--gold)}
  .label.light{color:#fff}
  .fill{font-family:"Oswald",sans-serif;font-weight:300;font-size:3.4px;line-height:1.5;color:var(--muted);text-transform:uppercase;letter-spacing:.02em}
  .fill.light{color:#cfcfcf}
  .fill + .fill{margin-top:3px}

  .footer{position:absolute;left:0;right:0;bottom:0;height:9px;background:var(--sand);display:flex;align-items:center;justify-content:space-between;padding:0 8px}
  .footer .logo{position:static;font-size:4.5px}
  .footer-note{font-family:"Oswald",sans-serif;font-size:3px;color:#fff;letter-spacing:.05em;text-transform:uppercase}

  .icon{width:10px;height:10px;border-radius:50%;background:var(--slate);display:flex;align-items:center;justify-content:center;flex:none}
  .icon.gold{background:var(--gold)}
  .icon.white{background:#fff}
  .icon.sq{border-radius:1.5px}
  .icon svg{width:6px;height:6px}

  .row{position:absolute;display:flex;gap:4px;align-items:flex-start}
  .photo{position:absolute}

  /* cover / quote */
  .quote-mark{position:absolute;left:50%;top:36px;width:22px;height:22px;margin-left:-11px;border-radius:50%;background:var(--gold);display:flex;align-items:center;justify-content:center}
  .quote{position:absolute;left:0;right:0;text-align:center;font-family:"Bebas Neue",sans-serif;color:#fff;font-size:7.6px;line-height:1.5;letter-spacing:.02em}
  .cite{position:absolute;left:0;right:0;text-align:center;font-family:"Bebas Neue",sans-serif;color:#cfcfcf;font-size:3.8px}

  /* previous work */
  .badge{position:absolute;border:1px solid #9b9b9b}
  .badge.round{border-radius:50%}
  .badge.pill{border-radius:8px}
  .badge.solid{background:#8f8f8f;border:none}
  .work-box{position:absolute;left:76px;top:62px;width:145px;height:40px;background:var(--ink);display:flex;align-items:center;justify-content:center;font-family:"Bebas Neue",sans-serif;color:#fff;font-size:10px}

  .tile{position:absolute;width:83px;height:48px;padding:6px}
  .tile.gold{background:var(--gold)}
  .tile.grey{background:var(--smoke)}
  .tile.dark{background:var(--coal)}

  .bar{position:absolute;left:150px;width:134px;height:22px;display:flex;align-items:center;gap:5px;padding:0 6px}
  .bar .num{font-family:"Bebas Neue",sans-serif;color:#fff;font-size:15px;line-height:1;padding-right:5px;border-right:1px solid #fff}
  .bar.grey{background:var(--smoke)}
  .bar.gold{background:var(--gold)}
  .bar.dark{background:var(--coal)}

  .step-num{width:8px;height:8px;border-radius:50%;background:var(--ink);color:#fff;font-family:"Bebas Neue",sans-serif;font-size:4.5px;display:flex;align-items:center;justify-content:center;flex:none}
</style>
</head>
<body>
<main class="deck">

  <!-- 1 cover black -->
  <section class="slide bg-black">
    <div class="logo light center" style="font-size:14px"><span class="logo-square"></span><span>Fernhollow Advisory</span></div>
  </section>

  <!-- 2 cover framed -->
  <section class="slide">
    <div class="abs" style="inset:6px;border:1.5px solid var(--ink)"></div>
    <div class="logo" style="left:28px;top:60px;font-size:14px"><span class="logo-square"></span><span>Fernhollow Advisory</span></div>
    <div class="display" style="left:28px;top:100px;font-size:13px">Your title of presentation goes here</div>
    <div class="subline" style="left:28px;top:115px">Your subtitle goes here</div>
  </section>

  <!-- 3 cover grey -->
  <section class="slide bg-ash">
    <div class="logo" style="left:36px;top:52px;font-size:14px"><span class="logo-square"></span><span>Fernhollow Advisory</span></div>
    <div class="rule" style="left:36px;top:81px;width:160px"></div>
    <div class="display" style="left:36px;top:87px;font-size:12px">Your title goes here</div>
    <div class="subline" style="left:36px;top:99px">Your subtitle goes here</div>
  </section>

  <!-- 4 cover gold -->
  <section class="slide bg-gold">
    <div class="logo" style="left:153px;top:84px;font-size:14px"><span class="logo-square"></span><span>Fernhollow Advisory</span></div>
    <div class="rule" style="left:150px;right:0;top:113px;background:#fff"></div>
    <div class="display" style="left:153px;top:118px;font-size:12px">Your title goes here</div>
    <div class="subline" style="left:153px;top:130px">Your subtitle goes here</div>
  </section>

  <!-- 5 quote -->
  <section class="slide bg-black">
    <div class="quote-mark"><svg width="12" height="10" viewBox="0 0 12 10"><path d="M1 9V5C1 2.5 2.5 1 5 1v2C3.8 3 3.3 3.8 3.3 5H5v4zM7 9V5c0-2.5 1.5-4 4-4v2c-1.2 0-1.7.8-1.7 2H11v4z" fill="#fff"/></svg></div>
    <p class="quote" style="top:74px">Coming together is a beginning.<br>Keeping together is progress.<br>Working together is success.</p>
    <p class="cite" style="top:122px">- Harlan Voss -</p>
  </section>

  <!-- 6 agenda -->
  <section class="slide">
    <h2 class="title">Our agenda</h2>
    <div class="row" style="left:38px;top:44px"><span class="icon sq"><svg viewBox="0 0 6 6"><circle cx="3" cy="3" r="2.3" fill="none" stroke="#fff" stroke-width=".6"/><path d="M3 1.8V3h1" stroke="#fff" stroke-width=".6" fill="none"/></svg></span><div style="width:80px"><p class="label">Agenda one</p><p class="label gold" style="font-size:3.4px">9:00</p><p class="fill">Short notes on the aim, the team and the next step.</p></div></div>
    <div class="row" style="left:38px;top:78px"><span class="icon sq"><svg viewBox="0 0 6 6"><circle cx="3" cy="3" r="2.3" fill="none" stroke="#fff" stroke-width=".6"/><path d="M3 1.8V3h1" stroke="#fff" stroke-width=".6" fill="none"/></svg></span><div style="width:80px"><p class="label">Agenda two</p><p class="label gold" style="font-size:3.4px">9:00</p><p class="fill">Short notes on the aim, the team and the next step.</p></div></div>
    <div class="row" style="left:38px;top:112px"><span class="icon sq"><svg viewBox="0 0 6 6"><circle cx="3" cy="3" r="2.3" fill="none" stroke="#fff" stroke-width=".6"/><path d="M3 1.8V3h1" stroke="#fff" stroke-width=".6" fill="none"/></svg></span><div style="width:80px"><p class="label">Agenda three</p><p class="label gold" style="font-size:3.4px">9:00</p><p class="fill">Short notes on the aim, the team and the next step.</p></div></div>
    <div class="row" style="left:160px;top:44px"><span class="icon sq"><svg viewBox="0 0 6 6"><circle cx="3" cy="3" r="2.3" fill="none" stroke="#fff" stroke-width=".6"/><path d="M3 1.8V3h1" stroke="#fff" stroke-width=".6" fill="none"/></svg></span><div style="width:80px"><p class="label">Agenda four</p><p class="label gold" style="font-size:3.4px">9:00</p><p class="fill">Short notes on the aim, the team and the next step.</p></div></div>
    <div class="row" style="left:160px;top:78px"><span class="icon sq"><svg viewBox="0 0 6 6"><circle cx="3" cy="3" r="2.3" fill="none" stroke="#fff" stroke-width=".6"/><path d="M3 1.8V3h1" stroke="#fff" stroke-width=".6" fill="none"/></svg></span><div style="width:80px"><p class="label">Agenda five</p><p class="label gold" style="font-size:3.4px">9:00</p><p class="fill">Short notes on the aim, the team and the next step.</p></div></div>
    <div class="row" style="left:160px;top:112px"><span class="icon sq"><svg viewBox="0 0 6 6"><circle cx="3" cy="3" r="2.3" fill="none" stroke="#fff" stroke-width=".6"/><path d="M3 1.8V3h1" stroke="#fff" stroke-width=".6" fill="none"/></svg></span><div style="width:80px"><p class="label">Agenda six</p><p class="label gold" style="font-size:3.4px">9:00</p><p class="fill">Short notes on the aim, the team and the next step.</p></div></div>
    <footer class="footer"><div class="logo"><span class="logo-square"></span><span>Fernhollow Advisory</span></div><span class="footer-note">Fernhollow Advisory</span></footer>
  </section>

  <!-- 7 about us -->
  <section class="slide">
    <div class="photo" role="img" aria-label="Black and white photo of a domed cathedral above a city footbridge" style="left:0;top:0;width:210px;height:166px;background:linear-gradient(160deg,#d8d8d8 0%,#8a8a8a 45%,#3c3c3c 100%)"></div>
    <div class="abs" style="left:150px;top:38px;width:146px;height:86px;background:rgba(62,62,62,.94);padding:12px 12px">
      <p class="display" style="position:static;color:#fff;font-size:11px;margin-bottom:6px">About us</p>
      <p class="fill light">We turn research into clear plans that help health and science brands reach the right buyers with a sharp, honest story.</p>
      <p class="fill light">Short notes on the aim, the team and the next step.</p>
    </div>
    <footer class="footer"><div class="logo"><span class="logo-square"></span><span>Fernhollow Advisory</span></div><span class="footer-note">Fernhollow Advisory</span></footer>
  </section>

  <!-- 8 our services -->
  <section class="slide">
    <h2 class="title">Our services</h2>
    <div class="abs" style="left:28px;top:38px;width:115px;height:72px;background:var(--ash)"></div>
    <div class="logo" style="left:42px;top:70px;font-size:10px"><span class="logo-square"></span><span>Fernhollow Advisory</span></div>
    <div class="abs" style="left:28px;top:116px;width:112px"><p class="label">Your title goes here</p><p class="fill">We turn research into clear plans that help health and science brands reach the right buyers with a sharp, honest story.</p></div>
    <div class="row" style="left:162px;top:40px"><span class="icon"><svg viewBox="0 0 6 6"><path d="M1 5V3.5M2.5 5V2.5M4 5V1.5" stroke="#fff" stroke-width=".7"/></svg></span><div style="width:105px"><p class="label">Service number one</p><p class="fill">Short notes on the aim, the team and the next step.</p></div></div>
    <div class="row" style="left:162px;top:75px"><span class="icon"><svg viewBox="0 0 6 6"><path d="M1 5L4.5 1.5M3.5 1l1.5 1.5" stroke="#fff" stroke-width=".7"/></svg></span><div style="width:105px"><p class="label">Service number two</p><p class="fill">Short notes on the aim, the team and the next step.</p></div></div>
    <div class="row" style="left:162px;top:108px"><span class="icon"><svg viewBox="0 0 6 6"><circle cx="2.6" cy="2.6" r="1.6" fill="none" stroke="#fff" stroke-width=".7"/><path d="M3.8 3.8L5.2 5.2" stroke="#fff" stroke-width=".7"/></svg></span><div style="width:105px"><p class="label">Service number three</p><p class="fill">Short notes on the aim, the team and the next step.</p></div></div>
    <footer class="footer"><div class="logo"><span class="logo-square"></span><span>Fernhollow Advisory</span></div><span class="footer-note">Fernhollow Advisory</span></footer>
  </section>

  <!-- 9 quote area -->
  <section class="slide">
    <h2 class="title">Quote area</h2>
    <div class="abs" style="left:0;right:0;top:38px;height:98px;background:var(--coal)"></div>
    <div class="photo" role="img" aria-label="Night photo of a city bridge with light trails from traffic" style="left:148px;right:0;top:38px;height:98px;background:linear-gradient(110deg,#2b2b33 0%,#5a4d52 45%,#c9c3c6 70%,#3b3c46 100%)"></div>
    <p class="quote" style="left:20px;right:auto;top:60px;text-align:left;font-size:6px;line-height:1.45">“ Coming together is a beginning.<br>Keeping together is progress.<br>Working together is success. ”</p>
    <p class="cite" style="left:24px;right:auto;top:98px;text-align:left">- Harlan Voss -</p>
    <footer class="footer"><div class="logo"><span class="logo-square"></span><span>Fernhollow Advisory</span></div><span class="footer-note">Fernhollow Advisory</span></footer>
  </section>

  <!-- 10 previous work -->
  <section class="slide">
    <span class="badge solid" style="left:14px;top:20px;width:44px;height:14px"></span>
    <span class="badge pill" style="left:92px;top:16px;width:44px;height:22px"></span>
    <span class="badge solid" style="left:168px;top:18px;width:42px;height:18px"></span>
    <span class="badge pill" style="left:240px;top:22px;width:44px;height:10px"></span>
    <span class="badge round" style="left:20px;top:62px;width:26px;height:26px"></span>
    <span class="badge pill solid" style="left:244px;top:76px;width:42px;height:10px;background:#b9b9b9"></span>
    <div class="work-box">Our previous work</div>
    <span class="badge round" style="left:22px;top:118px;width:22px;height:22px"></span>
    <span class="badge round" style="left:98px;top:116px;width:28px;height:28px"></span>
    <span class="badge solid" style="left:166px;top:124px;width:44px;height:14px"></span>
    <span class="badge" style="left:244px;top:118px;width:38px;height:24px"></span>
  </section>

  <!-- 11 text area -->
  <section class="slide">
    <h2 class="title">Text area</h2>
    <p class="header" style="left:12px;top:42px;width:272px">This is place for your header text. Insert your text here, just replace this text with your own text</p>
    <div class="abs" style="left:12px;top:62px;width:272px">
      <p class="fill">We turn research into clear plans that help health and science brands reach the right buyers with a sharp, honest story.</p>
      <p class="fill" style="margin-top:7px">We turn research into clear plans that help health and science brands reach the right buyers with a sharp, honest story.</p>
      <p class="fill" style="margin-top:7px">Short notes on the aim, the team and the next step.</p>
    </div>
    <footer class="footer"><div class="logo"><span class="logo-square"></span><span>Fernhollow Advisory</span></div><span class="footer-note">Fernhollow Advisory</span></footer>
  </section>

  <!-- 12 vision & mission -->
  <section class="slide">
    <h2 class="title">Our vision &amp; mission</h2>
    <div class="abs" style="left:0;right:0;top:38px;height:108px;background:var(--coal)"></div>
    <div class="abs" style="left:14px;top:50px;width:120px">
      <p class="label light" style="font-size:6px">• Our vision:</p>
      <p class="label light" style="font-size:5.4px;margin:4px 0 5px;width:80px">Go to the next level without look in the past</p>
      <p class="fill light">We turn research into clear plans that help health and science brands reach the right buyers with a sharp, honest story.</p>
    </div>
    <p class="label light abs" style="left:162px;top:50px;font-size:6px">• Our missions:</p>
    <div class="row" style="left:162px;top:64px"><span class="icon white"><svg viewBox="0 0 6 6"><circle cx="3" cy="3" r="1.6" fill="var(--gold)"/></svg></span><div style="width:110px"><p class="label light">Your text here</p><p class="fill light">Short notes on the aim, the team and the next step.</p></div></div>
    <div class="row" style="left:162px;top:88px"><span class="icon white"><svg viewBox="0 0 6 6"><circle cx="3" cy="3" r="1.6" fill="var(--gold)"/></svg></span><div style="width:110px"><p class="label light">Your text here</p><p class="fill light">Short notes on the aim, the team and the next step.</p></div></div>
    <div class="row" style="left:162px;top:112px"><span class="icon white"><svg viewBox="0 0 6 6"><circle cx="3" cy="3" r="1.6" fill="var(--gold)"/></svg></span><div style="width:110px"><p class="label light">Your text here</p><p class="fill light">Short notes on the aim, the team and the next step.</p></div></div>
    <footer class="footer"><div class="logo"><span class="logo-square"></span><span>Fernhollow Advisory</span></div><span class="footer-note">Fernhollow Advisory</span></footer>
  </section>

  <!-- 13 text area framed -->
  <section class="slide bg-coal">
    <div class="abs" style="left:10px;right:10px;top:10px;bottom:10px;background:var(--paper)"></div>
    <h2 class="title" style="left:24px;top:26px;font-size:12px">Text area</h2>
    <div class="logo" style="left:222px;top:30px;font-size:7px"><span class="logo-square"></span><span>Fernhollow Advisory</span></div>
    <p class="header" style="left:24px;top:60px;width:250px;font-size:5px">This is place for your header text. Insert your text here, just replace this text with your own text</p>
    <div class="abs" style="left:24px;top:80px;width:250px">
      <p class="fill">We turn research into clear plans that help health and science brands reach the right buyers with a sharp, honest story.</p>
      <p class="fill" style="margin-top:6px">Short notes on the aim, the team and the next step.</p>
      <p class="fill" style="margin-top:6px">We turn research into clear plans that help health and science brands reach the right buyers with a sharp, honest story.</p>
    </div>
  </section>

  <!-- 14 steps -->
  <section class="slide">
    <div class="abs" style="left:0;top:0;width:150px;height:112px;background:var(--sand)"></div>
    <div class="logo" style="left:30px;top:48px;font-size:13px"><span class="logo-square"></span><span>Fernhollow Advisory</span></div>
    <div class="row" style="left:30px;top:124px"><span class="step-num">1</span><div style="width:80px"><p class="label">Your text goes here</p><p class="fill">Short notes on the aim, the team and the next step.</p></div></div>
    <div class="row" style="left:170px;top:32px"><span class="step-num">2</span><div style="width:90px"><p class="label">Your text goes here</p><p class="fill">Short notes on the aim, the team and the next step.</p></div></div>
    <div class="row" style="left:170px;top:72px"><span class="step-num">3</span><div style="width:90px"><p class="label">Your text goes here</p><p class="fill">Short notes on the aim, the team and the next step.</p></div></div>
    <div class="row" style="left:170px;top:108px"><span class="step-num">4</span><div style="width:90px"><p class="label">Your text goes here</p><p class="fill">Short notes on the aim, the team and the next step.</p></div></div>
    <footer class="footer"><div class="logo"><span class="logo-square"></span><span>Fernhollow Advisory</span></div><span class="footer-note">Fernhollow Advisory</span></footer>
  </section>

  <!-- 15 image grid -->
  <section class="slide">
    <h2 class="title">Your title goes here</h2>
    <div class="photo" role="img" aria-label="Photo of a bridge tower at dusk" style="left:20px;top:40px;width:83px;height:48px;background:linear-gradient(180deg,#7d8ea3,#3e4a58)"></div>
    <div class="tile gold" style="left:106px;top:40px"><p class="label light">Heading goes here</p><p class="fill light">Short notes on the aim, the team and the next step.</p></div>
    <div class="photo" role="img" aria-label="Black and white photo of a cathedral dome" style="left:192px;top:40px;width:83px;height:48px;background:linear-gradient(180deg,#d0d0d0,#5a5a5a)"></div>
    <div class="tile grey" style="left:20px;top:91px"><p class="label light">Heading goes here</p><p class="fill light">Short notes on the aim, the team and the next step.</p></div>
    <div class="photo" role="img" aria-label="Black and white photo of a city skyline" style="left:106px;top:91px;width:83px;height:48px;background:linear-gradient(180deg,#bfbfbf,#4d4d4d)"></div>
    <div class="tile dark" style="left:192px;top:91px"><p class="label light">Heading goes here</p><p class="fill light">Short notes on the aim, the team and the next step.</p></div>
    <footer class="footer"><div class="logo"><span class="logo-square"></span><span>Fernhollow Advisory</span></div><span class="footer-note">Fernhollow Advisory</span></footer>
  </section>

  <!-- 16 photo with list -->
  <section class="slide bg-coal">
    <div class="photo" role="img" aria-label="Black and white photo of a domed cathedral under a cloudy sky" style="left:0;top:0;width:150px;height:166px;background:linear-gradient(165deg,#e0e0e0 0%,#8c8c8c 50%,#2e2e2e 100%)"></div>
    <p class="header" style="left:160px;top:20px;width:122px;color:#fff;font-size:5.8px">This is place for your header text. Insert your text here, just replace this text with your own text</p>
    <div class="row" style="left:160px;top:64px"><svg width="9" height="9" viewBox="0 0 6 6"><circle cx="2.6" cy="2.6" r="1.7" fill="none" stroke="#fff" stroke-width=".7"/><path d="M3.8 3.8L5.4 5.4" stroke="#fff" stroke-width=".7"/></svg><div style="width:110px"><p class="label light" style="font-size:3.8px">Your text here</p><p class="fill light">Brief line about this point.</p></div></div>
    <div class="row" style="left:160px;top:88px"><svg width="9" height="9" viewBox="0 0 6 6"><path d="M1 5L4.5 1.5M3.5 1l1.5 1.5" stroke="#fff" stroke-width=".7"/></svg><div style="width:110px"><p class="label light" style="font-size:3.8px">Your text here</p><p class="fill light">Brief line about this point.</p></div></div>
    <div class="row" style="left:160px;top:112px"><svg width="9" height="9" viewBox="0 0 6 6"><rect x="1" y="1.5" width="4" height="3" rx=".5" fill="none" stroke="#fff" stroke-width=".6"/><circle cx="3" cy="3" r=".8" fill="#fff"/></svg><div style="width:110px"><p class="label light" style="font-size:3.8px">Your text here</p><p class="fill light">Brief line about this point.</p></div></div>
    <div class="row" style="left:160px;top:136px"><svg width="9" height="9" viewBox="0 0 6 6"><circle cx="3" cy="3" r="1.3" fill="none" stroke="#fff" stroke-width=".9"/><path d="M3 .5V1.5M3 4.5V5.5M.5 3H1.5M4.5 3H5.5" stroke="#fff" stroke-width=".8"/></svg><div style="width:110px"><p class="label light" style="font-size:3.8px">Your text here</p><p class="fill light">Brief line about this point.</p></div></div>
  </section>

  <!-- 17 two column -->
  <section class="slide">
    <h2 class="title">Two column description</h2>
    <p class="header" style="left:12px;top:42px;width:272px">This is place for your header text. Insert your text here, just replace this text with your own text</p>
    <div class="abs" style="left:12px;top:62px;width:128px"><p class="fill">We turn research into clear plans that help health and science brands reach the right buyers with a sharp, honest story.</p><p class="fill" style="margin-top:6px">Short notes on the aim, the team and the next step.</p></div>
    <div class="abs" style="left:154px;top:62px;width:128px"><p class="fill">We turn research into clear plans that help health and science brands reach the right buyers with a sharp, honest story.</p><p class="fill" style="margin-top:6px">Short notes on the aim, the team and the next step.</p></div>
    <footer class="footer"><div class="logo"><span class="logo-square"></span><span>Fernhollow Advisory</span></div><span class="footer-note">Fernhollow Advisory</span></footer>
  </section>

  <!-- 18 coffee break -->
  <section class="slide bg-black">
    <div class="photo" role="img" aria-label="Dark moody photo of a coffee cup on a table" style="inset:0;background:radial-gradient(ellipse at 70% 70%,#3a3a3a 0%,#1c1c1c 55%,#0e0e0e 100%)"></div>
    <div class="logo light" style="left:210px;top:32px;font-size:8px"><span class="logo-square"></span><span>Fernhollow Advisory</span></div>
    <svg class="abs" style="left:140px;top:82px" width="16" height="14" viewBox="0 0 16 14"><path d="M5 1c1 1-1 2 0 3M8 1c1 1-1 2 0 3" stroke="#fff" stroke-width=".8" fill="none"/><path d="M2 6h10v3a4 4 0 0 1-4 4H6a4 4 0 0 1-4-4z" fill="#fff"/><path d="M12 7h1.5a1.5 1.5 0 0 1 0 3H12" stroke="#fff" stroke-width="1" fill="none"/></svg>
    <p class="display" style="left:0;right:0;top:103px;text-align:center;color:#fff;font-size:9px">Coffee break</p>
    <p class="display" style="left:0;right:0;top:114px;text-align:center;color:#d0d0d0;font-size:3.8px">Back in 15 minutes</p>
  </section>

  <!-- 19 three column -->
  <section class="slide">
    <h2 class="title">Three column description</h2>
    <p class="header" style="left:12px;top:42px;width:272px">This is place for your header text. Insert your text here, just replace this text with your own text</p>
    <div class="abs" style="left:12px;top:62px;width:84px"><p class="fill">We turn research into clear plans that help health and science brands reach the right buyers with a sharp, honest story.</p><p class="fill" style="margin-top:6px">Short notes on the aim, the team and the next step.</p></div>
    <div class="abs" style="left:106px;top:62px;width:84px"><p class="fill">We turn research into clear plans that help health and science brands reach the right buyers with a sharp, honest story.</p><p class="fill" style="margin-top:6px">Short notes on the aim, the team and the next step.</p></div>
    <div class="abs" style="left:200px;top:62px;width:84px"><p class="fill">We turn research into clear plans that help health and science brands reach the right buyers with a sharp, honest story.</p><p class="fill" style="margin-top:6px">Short notes on the aim, the team and the next step.</p></div>
    <footer class="footer"><div class="logo"><span class="logo-square"></span><span>Fernhollow Advisory</span></div><span class="footer-note">Fernhollow Advisory</span></footer>
  </section>

  <!-- 20 services with numbered bars -->
  <section class="slide">
    <h2 class="title">Your title goes here</h2>
    <div class="abs" style="left:12px;top:38px;width:272px"><p class="label">Heading goes here</p><p class="fill">We turn research into clear plans that help health and science brands reach the right buyers with a sharp, honest story.</p></div>
    <div class="row" style="left:12px;top:66px"><span class="icon"><svg viewBox="0 0 6 6"><path d="M1 5V3.5M2.5 5V2.5M4 5V1.5" stroke="#fff" stroke-width=".7"/></svg></span><div style="width:110px"><p class="label">Service number one</p><p class="fill">Short notes on the aim, the team and the next step.</p></div></div>
    <div class="row" style="left:12px;top:94px"><span class="icon gold"><svg viewBox="0 0 6 6"><path d="M1 5L4.5 1.5M3.5 1l1.5 1.5" stroke="#fff" stroke-width=".7"/></svg></span><div style="width:110px"><p class="label gold">Service number two</p><p class="fill">Short notes on the aim, the team and the next step.</p></div></div>
    <div class="row" style="left:12px;top:122px"><span class="icon"><svg viewBox="0 0 6 6"><circle cx="2.6" cy="2.6" r="1.6" fill="none" stroke="#fff" stroke-width=".7"/><path d="M3.8 3.8L5.2 5.2" stroke="#fff" stroke-width=".7"/></svg></span><div style="width:110px"><p class="label">Service number three</p><p class="fill">Short notes on the aim, the team and the next step.</p></div></div>
    <div class="bar grey" style="top:66px"><span class="num">1</span><p class="fill light">Short notes on the aim, the team and the next step.</p></div>
    <div class="bar gold" style="top:94px"><span class="num">2</span><p class="fill light">Short notes on the aim, the team and the next step.</p></div>
    <div class="bar dark" style="top:122px"><span class="num">3</span><p class="fill light">Short notes on the aim, the team and the next step.</p></div>
    <footer class="footer"><div class="logo"><span class="logo-square"></span><span>Fernhollow Advisory</span></div><span class="footer-note">Fernhollow Advisory</span></footer>
  </section>

  <!-- 21 four bullets -->
  <section class="slide">
    <h2 class="title">Four bullets with paragraph</h2>
    <div class="row" style="left:12px;top:54px"><span class="icon gold"><svg viewBox="0 0 6 6"><circle cx="2.6" cy="2.6" r="1.6" fill="none" stroke="#fff" stroke-width=".7"/><path d="M3.8 3.8L5.2 5.2" stroke="#fff" stroke-width=".7"/></svg></span><div style="width:45px"><p class="label gold">Your text here</p><p class="fill">Brief line about this point.</p></div></div>
    <div class="row" style="left:76px;top:54px"><span class="icon"><svg viewBox="0 0 6 6"><path d="M1 5L4.5 1.5M3.5 1l1.5 1.5" stroke="#fff" stroke-width=".7"/></svg></span><div style="width:45px"><p class="label">Your text here</p><p class="fill">Brief line about this point.</p></div></div>
    <div class="row" style="left:12px;top:102px"><span class="icon"><svg viewBox="0 0 6 6"><circle cx="3" cy="3" r="1.3" fill="none" stroke="#fff" stroke-width=".9"/></svg></span><div style="width:45px"><p class="label">Your text here</p><p class="fill">Brief line about this point.</p></div></div>
    <div class="row" style="left:76px;top:102px"><span class="icon gold"><svg viewBox="0 0 6 6"><path d="M1 5L4.5 1.5M3.5 1l1.5 1.5" stroke="#fff" stroke-width=".7"/></svg></span><div style="width:45px"><p class="label gold">Your text here</p><p class="fill">Brief line about this point.</p></div></div>
    <div class="abs" style="left:165px;top:52px;width:118px"><p class="label" style="font-size:5.4px;margin-bottom:4px">Heading goes here</p><p class="fill">We turn research into clear plans that help health and science brands reach the right buyers with a sharp, honest story.</p><p class="fill" style="margin-top:6px">Short notes on the aim, the team and the next step.</p></div>
    <footer class="footer"><div class="logo"><span class="logo-square"></span><span>Fernhollow Advisory</span></div><span class="footer-note">Fernhollow Advisory</span></footer>
  </section>

</main>
</body>
</html>
```